Thistlewood Candles, Hand-poured scented soy candles

Create a logo and label design to use on my vintage country farmhouse style, all natural, hand poured soy candle jars and apothecaries. Candles will be labeled in 4 different sizes so design must be adaptable, clean, simple, telegraphic and invoke interest in the product. Think Black lettering on white or black on kraft brown. Thistlewood is the area code for New Hampshire where we make them. The labels will need a prominent area for the scent of the candle to be listed that the eyes are drawn to. Primitive country in design? Use of state attractions? Jars are a square mason style 8 ounce and 16 ounce. Tarts are a clamshell. Lids are a 70-400 series 2.5" label area. Candles are white in a clear glass jar, black lids. There will be label design sizes of 3"x 2.5" 2.5" round, 1.5"x2.5"

Target Market(s)

primitive country, farmhouse, vintage, general home decor

Contact Information for Business Card

Thistlewood Candles, all natural soy candles, hand-poured in New Hampshire, logo, phone, address. Possibly match the main label.

Logo Text

Thistlewood Candles, all natural soy candles, hand-poured in New Hampshire, area for scent description and size of container.

Font styles to use
Serif
Script

Colors

Designer to choose colors to be used in the design.

Requirements
Must have
• simple and clean, country farmhouse with a bit of vintage thrown in. possibly multiple fonts to distinguish info from scent name
Nice to have
• at this time I am open to suggestions
• Prefer scent names or brand name in an older script?
• older copperplate/Spencerian?
Should not have
• cluttered, busy, too modern, multiple colors

```html
<!DOCTYPE html>
<html lang="en">
<head>
<meta charset="utf-8">
<title>Thistlewood Candles – Label System</title>
<link rel="stylesheet" href="https://fonts.googleapis.com/css2?family=Libre+Caslon+Text&family=Josefin+Sans:wght@700&family=Pinyon+Script&family=Questrial&family=PT+Sans+Narrow&display=swap">
<style>
  :root {
    --paper: #ffffff;
    --ink: #0b0b0b;
    --kraft: #c9a986;
    --cut-line: #e0141b;
    --illustration-light: #d9d4cc;
    --illustration-dark: #3a3a3a;
    --illustration-kraft: #8c7358;
  }
  html, body {
    margin: 0;
    padding: 0;
    overflow: hidden;
  }
  body {
    width: 1200px;
    height: 1120px;
    background: var(--paper);
    position: relative;
  }
  .lid-badge, .label { position: absolute; display: block; }
  .lid-badge { left: 419px; top: 40px; width: 144px; height: 144px; }
  .label { width: 505px; height: 315px; }
  .label--kraft { left: 614px; top: 56px; }
  .label--white { left: 614px; top: 403px; }
  .label--black { left: 611px; top: 750px; }
  .size-note {
    position: absolute;
    left: 416px;
    top: 398px;
    margin: 0;
    font-family: "PT Sans Narrow", sans-serif;
    font-size: 22px;
    color: var(--ink);
  }
  .t-tagline, .t-origin {
    font-family: "Libre Caslon Text", serif;
    letter-spacing: 4px;
  }
  .t-tagline { font-size: 25px; }
  .t-origin { font-size: 23px; }
  .t-brand {
    font-family: "Josefin Sans", sans-serif;
    font-weight: 700;
  }
  .t-scent { font-family: "Pinyon Script", cursive; font-size: 104px; }
  .t-size { font-family: "Questrial", sans-serif; font-size: 25px; letter-spacing: 1px; }
  .cut-line { fill: none; stroke: var(--cut-line); stroke-width: 2; }
</style>
</head>
<body>

<svg class="lid-badge" viewBox="0 0 240 240" role="group" aria-label="Round lid label">
  <circle cx="120" cy="120" r="116" fill="none" stroke="var(--ink)" stroke-width="3" stroke-dasharray="6 4"/>
  <circle cx="120" cy="120" r="106" fill="var(--ink)"/>
  <text class="t-brand" x="120" y="116" text-anchor="middle" font-size="24" textLength="168" lengthAdjust="spacingAndGlyphs" fill="var(--paper)">THISTLEWOOD</text>
  <text class="t-brand" x="120" y="154" text-anchor="middle" font-size="26" textLength="140" lengthAdjust="spacingAndGlyphs" fill="var(--paper)">CANDLES</text>
</svg>

<p class="size-note">Size: 1,5 x 2,5</p>

<!-- Kraft label -->
<svg class="label label--kraft" viewBox="0 0 834 520" role="group" aria-label="Kraft jar label">
  <rect width="834" height="520" fill="var(--kraft)"/>
  <text class="t-tagline" x="418" y="60" text-anchor="middle" fill="var(--ink)">ALL NATURAL SOY CANDLES</text>
  <rect x="16" y="78" width="796" height="12" fill="var(--ink)"/>
  <rect x="472" y="86" width="206" height="122" fill="none" stroke="var(--ink)" stroke-width="3" stroke-dasharray="3 5"/>
  <rect x="484" y="86" width="184" height="112" fill="var(--ink)"/>
  <text class="t-brand" x="576" y="140" text-anchor="middle" font-size="24" textLength="164" lengthAdjust="spacingAndGlyphs" fill="var(--kraft)">THISTLEWOOD</text>
  <text class="t-brand" x="576" y="182" text-anchor="middle" font-size="27" textLength="148" lengthAdjust="spacingAndGlyphs" fill="var(--kraft)">CANDLES</text>
  <rect x="40" y="170" width="334" height="198" rx="8" fill="var(--illustration-kraft)" role="img" aria-label="Ink sketch of a country farmhouse among trees"/>
  <text class="t-scent" x="415" y="322" fill="var(--ink)">Flavour</text>
  <line x1="8" y1="422" x2="822" y2="422" stroke="var(--ink)" stroke-width="2" stroke-dasharray="6 4"/>
  <text class="t-origin" x="55" y="452" fill="var(--ink)">HAND-POURED IN NEW HAMPSHIRE</text>
  <text class="t-size" x="634" y="452" fill="var(--ink)">· · ·</text>
  <text class="t-size" x="718" y="452" fill="var(--ink)">8 oz</text>
  <line x1="8" y1="466" x2="822" y2="466" stroke="var(--ink)" stroke-width="2" stroke-dasharray="6 4"/>
  <rect x="5" y="486" width="813" height="18" fill="var(--ink)"/>
  <rect class="cut-line" x="20" y="22" width="792" height="475" rx="30"/>
</svg>

<!-- White label -->
<svg class="label label--white" viewBox="0 0 834 520" role="group" aria-label="White jar label">
  <text class="t-tagline" x="418" y="60" text-anchor="middle" fill="var(--ink)">ALL NATURAL SOY CANDLES</text>
  <rect x="16" y="78" width="796" height="12" fill="var(--ink)"/>
  <rect x="472" y="86" width="206" height="122" fill="none" stroke="var(--ink)" stroke-width="3" stroke-dasharray="3 5"/>
  <rect x="484" y="86" width="184" height="112" fill="var(--ink)"/>
  <text class="t-brand" x="576" y="140" text-anchor="middle" font-size="24" textLength="164" lengthAdjust="spacingAndGlyphs" fill="var(--paper)">THISTLEWOOD</text>
  <text class="t-brand" x="576" y="182" text-anchor="middle" font-size="27" textLength="148" lengthAdjust="spacingAndGlyphs" fill="var(--paper)">CANDLES</text>
  <rect x="40" y="170" width="334" height="198" rx="8" fill="var(--illustration-light)" role="img" aria-label="Ink sketch of a country farmhouse among trees"/>
  <text class="t-scent" x="415" y="322" fill="var(--ink)">Flavour</text>
  <line x1="8" y1="422" x2="822" y2="422" stroke="var(--ink)" stroke-width="2" stroke-dasharray="6 4"/>
  <text class="t-origin" x="55" y="452" fill="var(--ink)">HAND-POURED IN NEW HAMPSHIRE</text>
  <text class="t-size" x="634" y="452" fill="var(--ink)">· · ·</text>
  <text class="t-size" x="718" y="452" fill="var(--ink)">8 oz</text>
  <line x1="8" y1="466" x2="822" y2="466" stroke="var(--ink)" stroke-width="2" stroke-dasharray="6 4"/>
  <rect x="5" y="486" width="813" height="18" fill="var(--ink)"/>
  <rect class="cut-line" x="20" y="22" width="792" height="475" rx="30"/>
</svg>

<!-- Black label -->
<svg class="label label--black" viewBox="0 0 834 520" role="group" aria-label="Black jar label">
  <rect width="834" height="520" fill="var(--ink)"/>
  <text class="t-tagline" x="418" y="60" text-anchor="middle" fill="var(--paper)">ALL NATURAL SOY CANDLES</text>
  <rect x="16" y="78" width="796" height="12" fill="var(--paper)"/>
  <rect x="472" y="86" width="206" height="122" fill="none" stroke="var(--paper)" stroke-width="3" stroke-dasharray="3 5"/>
  <rect x="484" y="86" width="184" height="112" fill="var(--paper)"/>
  <text class="t-brand" x="576" y="140" text-anchor="middle" font-size="24" textLength="164" lengthAdjust="spacingAndGlyphs" fill="var(--ink)">THISTLEWOOD</text>
  <text class="t-brand" x="576" y="182" text-anchor="middle" font-size="27" textLength="148" lengthAdjust="spacingAndGlyphs" fill="var(--ink)">CANDLES</text>
  <rect x="40" y="170" width="334" height="198" rx="8" fill="var(--illustration-dark)" role="img" aria-label="White line sketch of a country farmhouse among trees"/>
  <text class="t-scent" x="415" y="322" fill="var(--paper)">Flavour</text>
  <line x1="8" y1="422" x2="822" y2="422" stroke="var(--paper)" stroke-width="2" stroke-dasharray="6 4"/>
  <text class="t-origin" x="55" y="452" fill="var(--paper)">HAND-POURED IN NEW HAMPSHIRE</text>
  <text class="t-size" x="634" y="452" fill="var(--paper)">· · ·</text>
  <text class="t-size" x="718" y="452" fill="var(--paper)">8 oz</text>
  <line x1="8" y1="466" x2="822" y2="466" stroke="var(--paper)" stroke-width="2" stroke-dasharray="6 4"/>
  <rect x="5" y="486" width="813" height="18" fill="var(--paper)"/>
  <rect class="cut-line" x="20" y="22" width="792" height="475" rx="30"/>
</svg>

</body>
</html>
```